M&A Advisory firm needs elegant and powerful letterhead

We need a powerful but elegant letterhead to engage with the international financial industry.

Target Market(s)

New York and International Financial Industry

Industry/Entity Type

Finance

Font styles to use
Other font styles liked:
• Poppins

Requirements
Must have
• 482 W 71st Street 14th Floor New York, NY 10157 O: +1 (212) 555 0147 F: +1 (212) 555 0182

```html
<!DOCTYPE html>
<html lang="en">
<head>
<meta charset="utf-8">
<title>Norvane Letterhead</title>
<link rel="stylesheet" href="https://fonts.googleapis.com/css2?family=Poppins:wght@400;500&family=Open+Sans:wght@400&display=swap">
<style>
  :root {
    --brand-blue: #0b5596;
    --ink-grey: #8a8a8a;
    --paper: #ffffff;
    --backdrop: #d3d5d5;
    --footer-text: #ffffff;
  }
  * { margin: 0; padding: 0; box-sizing: border-box; }
  html, body { width: 1200px; height: 686px; overflow: hidden; }
  body {
    background: var(--backdrop);
    display: flex;
    align-items: center;
    justify-content: center;
  }
  .letterhead {
    position: relative;
    width: 496px;
    height: 642px;
    background: var(--paper);
    overflow: hidden;
  }
  .brand {
    position: absolute;
    top: 34px;
    left: 40px;
  }
  .brand-row {
    display: flex;
    align-items: center;
    gap: 10px;
  }
  .brand-dot {
    width: 22px;
    height: 22px;
    border-radius: 50%;
    background: var(--brand-blue);
  }
  .brand-name {
    font-family: "Poppins", sans-serif;
    font-weight: 400;
    font-size: 34px;
    letter-spacing: 2px;
    line-height: 1;
    color: var(--brand-blue);
  }
  .brand-tagline {
    margin-top: 4px;
    margin-left: 32px;
    font-family: "Poppins", sans-serif;
    font-size: 8.5px;
    letter-spacing: 3.6px;
    color: var(--ink-grey);
  }
  .footer-band {
    position: absolute;
    left: 0;
    right: 0;
    bottom: 0;
    height: 92px;
    background: var(--brand-blue);
    padding: 14px 0 0 26px;
    color: var(--footer-text);
    font-family: "Open Sans", sans-serif;
    font-size: 12.5px;
    line-height: 17px;
  }
  .contact-line {
    display: flex;
    align-items: flex-start;
    gap: 8px;
  }
  .contact-icon {
    width: 11px;
    height: 11px;
    margin-top: 3px;
    flex: none;
  }
  .contact-address span { display: block; }
</style>
</head>
<body>
  <main class="letterhead">
    <header class="brand">
      <div class="brand-row">
        <span class="brand-dot"></span>
        <span class="brand-name">NORVANE</span>
      </div>
      <p class="brand-tagline">Bridging Every Deal</p>
    </header>

    <footer class="footer-band">
      <div class="contact-line contact-address">
        <svg class="contact-icon" viewBox="0 0 12 12" aria-hidden="true">
          <path d="M6 0.5a4 4 0 0 0-4 4c0 3 4 7 4 7s4-4 4-7a4 4 0 0 0-4-4z" fill="none" stroke="currentColor" stroke-width="1.2"/>
          <circle cx="6" cy="4.5" r="1.4" fill="currentColor"/>
        </svg>
        <p><span>482 W 71st Street 14th Floor</span><span>New York, NY 10157</span></p>
      </div>
      <div class="contact-line">
        <svg class="contact-icon" viewBox="0 0 12 12" aria-hidden="true">
          <path d="M2.5 1h2l1 2.8-1.3 1a6.5 6.5 0 0 0 3 3l1-1.3 2.8 1v2A1.5 1.5 0 0 1 9.5 11 8.5 8.5 0 0 1 1 2.5 1.5 1.5 0 0 1 2.5 1z" fill="currentColor"/>
        </svg>
        <p>+1 (212) 555 0147</p>
      </div>
      <div class="contact-line">
        <svg class="contact-icon" viewBox="0 0 12 12" aria-hidden="true">
          <rect x="3" y="1" width="6" height="3.5" fill="none" stroke="currentColor" stroke-width="1"/>
          <rect x="1" y="4.5" width="10" height="5" rx="1" fill="currentColor"/>
          <rect x="3" y="8" width="6" height="3" fill="currentColor" stroke="#0b5596" stroke-width="0.6"/>
        </svg>
        <p>+1 (212) 555 0182</p>
      </div>
    </footer>
  </main>
</body>
</html>
```